Business Card Design - Photographer

I am a landscape photographer and I require a business card design. 

I require two designs:
1)  a double sided business card
 and
b)  a single sided business card 

The single sided design can either be the same as the double sided (with just one side having all the information)....or it can be an entire new design. Its up to you.

My corporate colours are (CMYK):

Blue   69, 32, 0, 0
Grey  72,  64,  47,  31
Green  32,  2,  91,  0
Yellow   0, 19, 92, 0
Orange  0, 39, 75, 0

Colour space in final file should be in CMYK.

The details that need to be included on the card:

- Use the provided Logo
- Name: Wiktor Nowiradzki
- Email:   sales@framesbywiktor.com.au
- Website:    framesbywiktor.com.au
- Twitter:    twitter.com/framesbywiktor
- Facebook:   facebook.com/framesbywiktor
- Mobile  0419 356 782

Please use the attached template to design the logo to the specified size, including the marked bleed lines. I have also attached my logo in PNG (transparent background) and ai format for you to use.

The final file should be:
- Photoshop version with layers so I can edit the name/text etc. All non vector files should be high resolution at 1039 x 697 pixels at 300 dpi.

I also require a file as:
- Vector based PDF

Anyway questions please contact me.

Thank you

Industry/Entity Type

Landscape

Logo styles of interest
Pictorial/Combination Logo
Abstract Logo
Wordmark Logo
Lettermark Logo
Requirements
Must have
• The details that need to be included on the card:

- Use the provided Logo
- Name: Wiktor Nowiradzki
- Email: sales@framesbywiktor.com.au
- Website: framesbywiktor.com.au
- Twitter: twitter.com/framesbywiktor
- Facebook: facebook.com/framesbywiktor
- Mobile 0419 356 782

```html
<!DOCTYPE html>
<html lang="en">
<head>
<meta charset="utf-8">
<title>Frames by Wiktor – Business Card</title>
<link rel="stylesheet" href="https://fonts.googleapis.com/css2?family=Cinzel:wght@500&family=PT+Sans+Narrow&display=swap">
<style>
  :root {
    --backdrop: #3b3430;
    --card-white: #ffffff;
    --slate: #4c5169;
    --slate-light: #8089ad;
    --slate-dark: #41455b;
    --ink: #3e4257;
    --snow-shade: #c9ccd8;
    --contact-text: #ffffff;
  }
  * { margin: 0; padding: 0; box-sizing: border-box; }
  html, body {
    width: 848px;
    height: 1200px;
    overflow: hidden;
    background: var(--backdrop);
  }
  .canvas {
    position: relative;
    width: 848px;
    height: 1200px;
  }
  .card {
    position: absolute;
    left: 153px;
    width: 544px;
    height: 340px;
    overflow: hidden;
  }
  .card--front {
    top: 225px;
    background: var(--card-white);
  }
  .card--back {
    top: 651px;
    height: 341px;
    background: radial-gradient(ellipse 360px 260px at 50% 10%, var(--slate-light) 0%, var(--slate) 60%, var(--slate-dark) 100%);
  }

  /* Front: brand lockup */
  .brand__dot {
    position: absolute;
    top: 22px;
    left: 247px;
    width: 50px;
    height: 50px;
    border-radius: 50%;
    background: var(--ink);
  }
  .brand__name {
    position: absolute;
    top: 103px;
    left: 0;
    width: 100%;
    text-align: center;
    font-family: "Cinzel", serif;
    font-weight: 500;
    font-size: 23px;
    letter-spacing: 1.6px;
    color: var(--ink);
    line-height: 1;
  }
  .brand__rule {
    position: absolute;
    top: 125px;
    left: 154px;
    width: 250px;
    height: 1px;
    background: var(--ink);
  }
  .brand__tagline {
    position: absolute;
    top: 129px;
    left: 0;
    width: 100%;
    text-align: center;
    font-family: "Cinzel", serif;
    font-weight: 500;
    font-size: 8px;
    letter-spacing: 2.2px;
    color: var(--ink);
    line-height: 1;
  }

  /* Front: landscape band and lower panel */
  .mountain-range {
    position: absolute;
    left: 0;
    top: 150px;
    width: 100%;
    height: 90px;
    background: linear-gradient(to bottom, var(--card-white) 0%, var(--snow-shade) 45%, var(--slate) 100%);
  }
  .front-panel {
    position: absolute;
    left: 0;
    top: 240px;
    width: 100%;
    height: 100px;
    background: radial-gradient(ellipse 330px 200px at 50% 20%, var(--slate-light) 0%, var(--slate) 65%, var(--slate-dark) 100%);
  }

  /* Back: contact details */
  .contact {
    position: absolute;
    top: 109px;
    left: 0;
    width: 100%;
    list-style: none;
    text-align: center;
    font-family: "PT Sans Narrow", sans-serif;
    font-size: 19px;
    line-height: 27px;
    color: var(--contact-text);
  }
</style>
</head>
<body>
<main class="canvas">
  <section class="card card--front" aria-label="Card front">
    <span class="brand__dot" aria-hidden="true"></span>
    <h1 class="brand__name">FRAMES BY WIKTOR</h1>
    <span class="brand__rule" aria-hidden="true"></span>
    <p class="brand__tagline">FINE ART PHOTOGRAPHY</p>
    <div class="mountain-range" role="img" aria-label="Snow-capped mountain range silhouette"></div>
    <div class="front-panel"></div>
  </section>

  <section class="card card--back" aria-label="Card back">
    <ul class="contact">
      <li>mobile: 0419 356 782</li>
      <li>website: framesbywiktor.com.au</li>
      <li>e-mail: sales@framesbywiktor.com.au</li>
      <li>twitter: twitter.com/framesbywiktor</li>
      <li>facebook: facebook.com/framesbywiktor</li>
    </ul>
  </section>
</main>
</body>
</html>
```